Business Card *

A business card design
Use the logo uploaded in the brief page.
You may use placeholders in your design layouts.
I will provide the actual business card details to the winning designer.

Logo
Place for contact info (name, title, phone, email, etc)

Requirements
Must have
• Logo

```html
<!DOCTYPE html>
<html lang="en">
<head>
<meta charset="utf-8">
<title>Kestrel Agriculture and Industry – Business Card</title>
<link href="https://fonts.googleapis.com/css2?family=Poppins:wght@400;500;700&display=swap" rel="stylesheet">
<style>
  :root {
    --backdrop: #2b2b2b;
    --card: #141414;
    --card-edge: #1d1d1d;
    --silver: #a9a9ab;
    --text-light: #c9c9cb;
    --green: #3cb44a;
    --faint: #1f1f1f;
  }
  * { box-sizing: border-box; margin: 0; padding: 0; }
  html, body { width: 1200px; height: 900px; overflow: hidden; }
  body {
    background: var(--backdrop);
    font-family: "Poppins", sans-serif;
    position: relative;
  }
  .card {
    position: absolute;
    width: 560px;
    height: 320px;
    border-radius: 22px;
    background: linear-gradient(135deg, var(--card-edge), var(--card) 60%);
    box-shadow: 0 14px 30px rgba(0,0,0,0.55);
    overflow: hidden;
  }
  .card--front { left: 90px; top: 80px; }
  .card--back { left: 550px; top: 500px; }

  .faint-mark {
    position: absolute;
    border-radius: 50%;
    border: 26px solid var(--faint);
  }
  .card--front .faint-mark { width: 300px; height: 300px; left: -40px; top: 50px; }
  .card--back .faint-mark { width: 240px; height: 240px; right: -60px; top: -10px; }

  .brand {
    position: absolute;
    left: 0; right: 0;
    display: flex;
    align-items: center;
    justify-content: center;
    gap: 12px;
  }
  .brand__dot {
    width: 34px; height: 34px;
    border-radius: 50%;
    background: var(--green);
  }
  .brand__name {
    font-weight: 700;
    font-size: 24px;
    letter-spacing: 1px;
    color: var(--silver);
    text-transform: uppercase;
    line-height: 1.1;
  }
  .card--front .brand { top: 128px; }
  .card--back .brand { top: 70px; }

  .details {
    position: absolute;
    left: 0; right: 0; top: 170px;
    display: flex;
    justify-content: center;
    align-items: center;
    gap: 20px;
  }
  .person { text-align: right; }
  .person__name {
    font-weight: 700;
    font-size: 22px;
    letter-spacing: 1.5px;
    color: var(--silver);
  }
  .person__title {
    font-size: 15px;
    color: var(--green);
    letter-spacing: 0.5px;
  }
  .divider {
    width: 2px; height: 92px;
    background: var(--silver);
  }
  .contact {
    list-style: none;
    font-size: 14px;
    line-height: 1.55;
    color: var(--text-light);
  }
  .contact__label { color: var(--green); margin-right: 4px; }
</style>
</head>
<body>
  <section class="card card--front" aria-label="Card front">
    <div class="faint-mark" aria-hidden="true"></div>
    <div class="brand">
      <span class="brand__dot" aria-hidden="true"></span>
      <span class="brand__name">Kestrel Agriculture and Industry</span>
    </div>
  </section>

  <section class="card card--back" aria-label="Card back">
    <div class="faint-mark" aria-hidden="true"></div>
    <div class="brand">
      <span class="brand__dot" aria-hidden="true"></span>
      <span class="brand__name">Kestrel Agriculture and Industry</span>
    </div>
    <div class="details">
      <div class="person">
        <p class="person__name">PRESIDENT NAME</p>
        <p class="person__title">CEO/OWNER</p>
      </div>
      <div class="divider" aria-hidden="true"></div>
      <ul class="contact">
        <li><span class="contact__label">P:</span>800 555 0142</li>
        <li><span class="contact__label">E:</span>info@kestrelagriculture.com</li>
        <li><span class="contact__label">A:</span>118 Alder Street NW</li>
        <li>Suite 210, Lakeview, MI 49000</li>
      </ul>
    </div>
  </section>
</body>
</html>
```